Business Card Design Project

I need a business card designed that is clean, simple and elegant.
I am a fashion and advertising photographer based in Cape Town and Durban South Africa.
check out my website: www.marlowvance.co.za for ideas
Updates
Hi all,
Thanks for your submissions so far!
Please note:
I want no more than than black, white and/or grey to be used.
I don't want any photos used.
I would like the card to be double sided.
I would like to continue the design similar to the past ones Ive used.
I hope this helps, please send me further questions should you have any.
many thanks!
Marlow
Hi,
Please have a look at the jpg I loaded(called inspiration) which is the direction or inspiration I am aiming at.
Also PLEASE remember NO PHOTOS to be included on the card
many thanks!!
Target Market(s)
You can look at my site to get a better understanding of the audience:
www.marlowvance.co.za
Industry/Entity Type
Advertising
Requirements
Must have
- Clean design which can also be used for a watermark on photographs
perhaps black background with white text/grey
company called: Marlow Vance Photography
Nice to have
- below I have added logos that I have used in the past.
Should not have
- pictures of cameras
tacky elements

```html
<!DOCTYPE html>
<html lang="en">
<head>
<meta charset="utf-8">
<title>Marlow Vance Photography – Business Card Concepts</title>
<link rel="stylesheet" href="https://fonts.googleapis.com/css2?family=Questrial&family=Arimo:wght@400&family=Roboto+Slab:wght@700&display=swap">
<style>
  :root {
    --page: #ffffff;
    --ink: #000000;
    --coal: #08090a;
    --slate: #4d4d4d;
    --white: #ffffff;
    --mist: #dcdcdc;
    --grey: #8a8a8a;
    --label: #9a9a9a;
  }
  * { margin: 0; padding: 0; box-sizing: border-box; }
  html, body { width: 1088px; height: 1200px; overflow: hidden; background: var(--page); }
  .sheet { position: relative; width: 1088px; height: 1200px; }

  .option-label {
    position: absolute; width: 60px; margin-left: -30px; text-align: center;
    font-family: "Roboto Slab", serif; font-weight: 700; font-size: 40px; line-height: 1;
    color: var(--label);
  }

  .card { position: absolute; width: 403px; height: 224px; overflow: hidden; }
  .card--rounded { border-radius: 20px; }
  .card--black { background: var(--ink); }
  .card--coal { background: var(--coal); }
  .card--slate { background: var(--slate); }

  .line { position: absolute; white-space: nowrap; line-height: 1; }
  .centered { left: 0; right: 0; text-align: center; }

  .wordmark { font-family: "Questrial", sans-serif; letter-spacing: 2px; }
  .name { font-family: "Questrial", sans-serif; letter-spacing: 1px; color: var(--white); }
  .studio { font-family: "Questrial", sans-serif; letter-spacing: 1px; color: var(--grey); }
  .contact { font-family: "Arimo", sans-serif; color: var(--white); }
  .site { font-family: "Arimo", sans-serif; color: var(--white); }

  .divider-v { position: absolute; left: 199px; top: 16px; width: 2px; height: 196px; background: var(--white); }
  .divider-h { position: absolute; left: 45px; top: 76px; width: 311px; height: 2px; background: var(--white); }

  .sprocket { position: absolute; left: 16px; right: 16px; height: 20px; display: flex; justify-content: space-between; }
  .sprocket span { width: 15px; height: 20px; background: var(--white); border-radius: 3px; }
</style>
</head>
<body>
<main class="sheet">

  <div class="option-label" style="left:281px; top:16px;">a</div>
  <div class="option-label" style="left:810px; top:16px;">b</div>
  <div class="option-label" style="left:299px; top:627px;">c</div>
  <div class="option-label" style="left:812px; top:627px;">d</div>

  <!-- Option A -->
  <section class="card card--rounded card--black" style="left:82px; top:71px;">
    <div class="line centered wordmark" style="top:92px; font-size:40px; color:var(--white);">MARLOW VANCE</div>
  </section>
  <section class="card card--rounded card--black" style="left:82px; top:328px;">
    <div class="line name" style="left:19px; top:84px; font-size:19px;">MARLOWVANCE</div>
    <div class="line studio" style="left:19px; top:103px; font-size:19px;">PHOTOGRAPHY</div>
    <div class="divider-v"></div>
    <div class="line contact" style="right:18px; top:85px; font-size:12px;">+27 (0)82 555 0147</div>
    <div class="line contact" style="right:18px; top:111px; font-size:12px;">+27 (0)31 555 0192</div>
    <div class="line contact" style="right:18px; top:133px; font-size:11px;">marlow@marlowvance.co.za</div>
    <div class="line site" style="right:18px; top:188px; font-size:16px;">www.marlowvance.co.za</div>
  </section>

  <!-- Option B -->
  <section class="card card--rounded card--black" style="left:608px; top:71px;">
    <div class="line centered wordmark" style="top:78px; font-size:30px; color:var(--white);">MARLOW VANCE</div>
    <div class="line centered name" style="top:143px; font-size:19px;">MARLOWVANCE</div>
    <div class="line centered studio" style="top:161px; font-size:19px;">PHOTOGRAPHY</div>
  </section>
  <section class="card card--rounded card--black" style="left:608px; top:329px;">
    <div class="line name" style="left:22px; top:45px; font-size:24px;">MARLOWVANCE</div>
    <div class="line contact" style="left:22px; top:89px; font-size:14px;">+27 (0)82 555 0147</div>
    <div class="line contact" style="left:22px; top:114px; font-size:14px;">+27 (0)31 555 0192</div>
    <div class="line contact" style="left:22px; top:141px; font-size:13px;">marlow@marlowvance.co.za</div>
    <div class="line site" style="left:22px; top:166px; font-size:16px;">www.marlowvance.co.za</div>
  </section>

  <!-- Option C -->
  <section class="card card--coal" style="left:85px; top:682px;">
    <div class="line centered wordmark" style="top:99px; font-size:26px; color:var(--mist);">MARLOW VANCE</div>
  </section>
  <section class="card card--coal" style="left:85px; top:939px;">
    <div class="sprocket" style="top:11px;"><span></span><span></span><span></span><span></span><span></span><span></span><span></span><span></span><span></span><span></span><span></span><span></span></div>
    <div class="line centered name" style="top:52px; font-size:19px;">MARLOWVANCE</div>
    <div class="line centered studio" style="top:72px; font-size:19px;">PHOTOGRAPHY</div>
    <div class="line centered contact" style="top:100px; font-size:12px;">+27 (0)82 555 0147</div>
    <div class="line centered contact" style="top:120px; font-size:12px;">+27 (0)31 555 0192</div>
    <div class="line centered contact" style="top:143px; font-size:11px;">marlow@marlowvance.co.za</div>
    <div class="line centered site" style="top:160px; font-size:16px;">www.marlowvance.co.za</div>
    <div class="sprocket" style="top:194px;"><span></span><span></span><span></span><span></span><span></span><span></span><span></span><span></span><span></span><span></span><span></span><span></span></div>
  </section>

  <!-- Option D -->
  <section class="card card--slate" style="left:608px; top:682px;">
    <div class="line centered wordmark" style="top:98px; font-size:28px; color:var(--ink);">MARLOW VANCE</div>
  </section>
  <section class="card card--slate" style="left:608px; top:939px;">
    <div class="line centered name" style="top:22px; font-size:23px; color:var(--mist);">MARLOWVANCE</div>
    <div class="line centered name" style="top:46px; font-size:23px; color:var(--ink);">PHOTOGRAPHY</div>
    <div class="divider-h"></div>
    <div class="line centered contact" style="top:100px; font-size:12px;">+27 (0)82 555 0147</div>
    <div class="line centered contact" style="top:128px; font-size:12px;">+27 (0)31 555 0192</div>
    <div class="line centered contact" style="top:157px; font-size:11px;">marlow@marlowvance.co.za</div>
    <div class="line centered site" style="top:182px; font-size:16px;">www.marlowvance.co.za</div>
  </section>

</main>
</body>
</html>
```